Aerial photo/video drone company needs new business card

Aerial visual company who offers photos and video services via drones.

We are QVL certified and work in the real estate, insurance, construction, and film industries.

I'm looking for a clean, professional, maybe even edgy design, that will be a conversation starter when networking.

I've included our logo, current business card, and font.

Our current business card is decent; albeit, I'm looking for something more unique. If you folks provide good designs, I'll definitely guarantee payment (and I'm not opposed to tipping if the design is above and beyond).

Target Market(s)

Insurance companies, real estate agents, construction companies, advertising & other creative agencies, and filmmakers/producers.

Industry/Entity Type

Business

Contact Information for Business Card

Company name pronounced air-a-vee.

Font styles to use
Other font styles liked:
• Font was uploaded; that or similar; not opposed to other fonts if they work well with the design

Requirements
Must have
• Clearly prominent logo; my name and title; phone number; email address; web address; mentioned "QVL Certified" or similar; should indicate "Aerial visual"
Nice to have
• Watermark of logo or otherwise
Should not have
• Pictures of drones or scenic shots

```html
<!DOCTYPE html>
<html lang="en">
<head>
<meta charset="utf-8">
<title>Skyvanta Business Card</title>
<link rel="stylesheet" href="https://fonts.googleapis.com/css2?family=Exo+2:wght@400;500;600;700&display=swap">
<style>
  :root {
    --backdrop: #e3e3e3;
    --card-white: #ffffff;
    --navy: #253857;
    --sky: #0a93dc;
    --sky-bright: #1ea0e6;
    --text-light: #ffffff;
  }
  * { box-sizing: border-box; margin: 0; padding: 0; }
  html, body {
    width: 1200px;
    height: 987px;
    overflow: hidden;
    background: var(--backdrop);
    font-family: "Exo 2", "Trebuchet MS", sans-serif;
  }
  .stage { position: relative; width: 1200px; height: 987px; }

  .card {
    position: absolute;
    left: 293px;
    width: 615px;
    height: 352px;
    box-shadow: 0 2px 5px rgba(0,0,0,0.22);
    overflow: hidden;
  }
  .card--front { top: 130px; background: var(--card-white); }
  .card--back { top: 505px; background: var(--sky); }

  /* front */
  .accent-bar {
    position: absolute;
    left: 0; top: 82px;
    width: 13px; height: 188px;
    background: var(--sky);
    clip-path: polygon(0 0, 100% 8px, 100% calc(100% - 8px), 0 100%);
  }
  .brand {
    position: absolute;
    left: 40px; top: 120px;
    width: 250px;
    display: flex;
    align-items: center;
    justify-content: center;
    gap: 10px;
  }
  .brand__dot {
    width: 18px; height: 18px;
    border-radius: 50%;
    background: var(--sky);
    flex: none;
  }
  .brand__name {
    font-size: 50px;
    font-weight: 600;
    color: var(--navy);
    letter-spacing: 1px;
    line-height: 1;
  }
  .contact-panel {
    position: absolute;
    left: 325px; top: 82px;
    width: 290px; height: 188px;
    background: var(--navy);
    clip-path: polygon(12px 0, 100% 0, 100% 100%, 12px 100%, 0 calc(100% - 10px), 0 10px);
    padding: 29px 0 0 32px;
    color: var(--text-light);
  }
  .contact-panel__name {
    font-size: 21px;
    font-weight: 600;
    color: var(--sky-bright);
    line-height: 1.1;
  }
  .contact-panel__title {
    font-size: 17px;
    font-weight: 400;
    margin-top: 2px;
    margin-bottom: 12px;
  }
  .contact-list { list-style: none; }
  .contact-list li {
    display: flex;
    align-items: center;
    gap: 9px;
    font-size: 16px;
    line-height: 23.5px;
  }
  .contact-list svg { width: 14px; height: 14px; flex: none; fill: var(--sky-bright); }

  /* back */
  .back-texture {
    position: absolute; inset: 0;
    background: linear-gradient(135deg, #0d97df 0%, #078fd8 100%);
  }
  .back-brand {
    position: absolute;
    left: 0; right: 0; top: 150px;
    display: flex;
    justify-content: center;
    align-items: center;
    gap: 14px;
  }
  .back-brand__dot {
    width: 22px; height: 22px;
    border-radius: 50%;
    background: var(--text-light);
  }
  .back-brand__name {
    font-size: 72px;
    font-weight: 600;
    color: var(--text-light);
    letter-spacing: 2px;
    line-height: 1;
  }
  .services {
    position: absolute;
    left: 0; right: 0; top: 278px;
    text-align: center;
    color: var(--text-light);
    font-size: 16.5px;
    line-height: 23px;
    letter-spacing: 0.2px;
  }
</style>
</head>
<body>
<div class="stage">

  <section class="card card--front">
    <div class="accent-bar"></div>
    <div class="brand">
      <span class="brand__dot"></span>
      <span class="brand__name">skyvanta</span>
    </div>
    <div class="contact-panel">
      <p class="contact-panel__name">Daniel K.Morrow</p>
      <p class="contact-panel__title">Owner . sUAS Pilot</p>
      <ul class="contact-list">
        <li>
          <svg viewBox="0 0 24 24" aria-hidden="true"><path d="M6.6 10.8a15.1 15.1 0 0 0 6.6 6.6l2.2-2.2c.3-.3.7-.4 1-.2 1.1.4 2.3.6 3.6.6.6 0 1 .4 1 1V20c0 .6-.4 1-1 1A17 17 0 0 1 3 4c0-.6.4-1 1-1h3.5c.6 0 1 .4 1 1 0 1.3.2 2.5.6 3.6.1.3 0 .7-.2 1z"/></svg>
          <span>555.014.2290</span>
        </li>
        <li>
          <svg viewBox="0 0 24 24" aria-hidden="true"><path d="M2 5h20v14H2z M3 6l9 7 9-7" stroke="#253857" stroke-width="1.6"/></svg>
          <span>dan@skyvanta.com</span>
        </li>
        <li>
          <svg viewBox="0 0 24 24" aria-hidden="true"><circle cx="12" cy="12" r="10"/><path d="M7 7c2 1 3 3 2 5s1 3 2 5M15 4c-1 2 0 3 2 4s2 3 3 3" stroke="#253857" stroke-width="1.6" fill="none"/></svg>
          <span>www.skyvanta.com</span>
        </li>
      </ul>
    </div>
  </section>

  <section class="card card--back">
    <div class="back-texture" role="img" aria-label="Subtle tone-on-tone geometric pattern in light and deep blue"></div>
    <div class="back-brand">
      <span class="back-brand__dot"></span>
      <span class="back-brand__name">skyvanta</span>
    </div>
    <p class="services">
      Aerial Visual for Real Estate &bull; Insurance &bull; Construction &bull; Film<br>
      QVL Part 107 Commercial sUAS Certified
    </p>
  </section>

</div>
</body>
</html>
```